Business Card Design/Stationary Design

We would like designers to submit cool, hip business card designs (plus stationary designs) for a new, upstart software development company located in Toronto.
If you have any questions, please email us.
For inspiration on designs:
http://cardmuse.example/cool-business-cards/
http://layoutnotes.example/2008/05/36-cool-business-cards-you-should%E2%80%99ve-seen.html
http://gigharbor.example/general/18-smokin-hot-business-card-designs/

Card info:

Selvakumar (Selv) Nadarasan

Founder and CEO

47 Brindle Court, Suite 311

Toronto, ON M4K 2T8

Phone: 647-512-7730

Mobile: 416-273-5094

Fax: 647-512-7731

Email: selvakumar.nadarasan@mailbrook.example

www.quendrix.example
Updates

Hi everyone,

In terms of all the designs I have seen so far, here is what I like:

1.  I really like the "back" part of this design.  The "front" looks pretty decent as well, but for the "front", look at #2 on this list.  I like that.

http://www.pitchboard.example/image.aspx?imageLocation=1000_10001_2000_image.jpg&type=design300px&whiteLabelCustId=9999

2. "Side 1" of this I like, the front needs to be reworked.

http://www.pitchboard.example/image.aspx?imageLocation=1000_10002_2000_image.png&type=design300px&whiteLabelCustId=9999

3. http://www.pitchboard.example/image.aspx?imageLocation=1000_10003_2000_image.jpg&type=design300px&whiteLabelCustId=9999

4. http://www.pitchboard.example/image.aspx?imageLocation=1000_10004_2000_image.jpg&type=design300px&whiteLabelCustId=9999

Target Market(s)

We are focused on enterprise customers right now, so businesses with a long-term goal of also reaching out to the consumer market as well.

Industry/Entity Type

Software

Requirements
Must have
• Must look cool, ultra-modern, clean and eye-catching. Must incorporate our logo and the colors found in the logo.

```html
<!DOCTYPE html>
<html lang="en">
<head>
<meta charset="utf-8">
<title>Quendrix Technologies Inc. — Stationery</title>
<link rel="stylesheet" href="https://fonts.googleapis.com/css2?family=Questrial&display=swap">
<style>
  :root {
    --paper: #ffffff;
    --edge: #c9c9c9;
    --shadow: #b4b4b4;
    --ink: #111111;
    --copy: #5a5a5a;
    --brand: #7fd600;
    --green-light: #b4f200;
    --green-mid: #74db00;
    --green-deep: #5cc400;
  }
  * { box-sizing: border-box; margin: 0; padding: 0; }
  html, body { width: 1073px; height: 1200px; overflow: hidden; background: var(--paper); }
  body { position: relative; font-family: "Questrial", sans-serif; color: var(--copy); }

  .band-fill {
    background: linear-gradient(90deg, var(--green-light) 0%, var(--green-mid) 55%, var(--green-deep) 100%);
  }

  /* Master lockup */
  .brand-master { position: absolute; left: 430px; top: 88px; display: flex; align-items: center; gap: 14px; }
  .brand-master .dot { width: 56px; height: 56px; border-radius: 50%; background: var(--brand); }
  .brand-master .name { font-size: 52px; line-height: 1; color: var(--ink); }
  .brand-master .sub { position: absolute; right: 0; top: 54px; font-size: 9.5px; letter-spacing: 0.6px; color: var(--ink); white-space: nowrap; }

  /* Small rotated lockup used on stationery */
  .lockup { position: absolute; transform: rotate(-20deg); transform-origin: left bottom; }
  .lockup .row { display: flex; align-items: center; gap: 6px; }
  .lockup .dot { width: 17px; height: 17px; border-radius: 50%; background: var(--brand); }
  .lockup .name { font-size: 15px; line-height: 1; color: var(--ink); }
  .lockup .sub { font-size: 3px; letter-spacing: 0.2px; color: var(--ink); margin: 1px 0 0 40px; white-space: nowrap; }
  .lockup .web { font-size: 7.6px; letter-spacing: 0.3px; color: var(--copy); margin: 3px 0 0 8px; white-space: nowrap; }

  .address { position: absolute; font-size: 8.4px; line-height: 10.5px; letter-spacing: 0.2px; white-space: nowrap; }

  /* Letterhead */
  .letterhead { position: absolute; left: 190px; top: 249px; width: 651px; height: 920px; background: var(--paper); border: 1px solid var(--edge); box-shadow: 2px 2px 0 var(--shadow); }
  .letterhead .band { position: absolute; left: 145px; top: 0; right: 0; height: 141px; }
  .letterhead .lockup { left: 26px; top: 42px; }
  .letterhead .address { left: 19px; top: 89px; }

  /* Envelope */
  .envelope { position: absolute; left: 40px; top: 606px; width: 651px; height: 307px; background: var(--paper); border: 1px solid var(--edge); box-shadow: 2px 2px 0 var(--shadow); }
  .envelope .band { position: absolute; left: 145px; top: 0; right: 0; height: 81px; }
  .envelope .lockup { left: 26px; top: 45px; }
  .envelope .address { left: 19px; top: 86px; }

  /* Business card — front */
  .card-front { position: absolute; left: 759px; top: 466px; width: 278px; height: 153px; background: var(--paper); border-radius: 0 9px 9px 0; box-shadow: 2px 2px 0 var(--shadow); }
  .card-front .lockup { left: 14px; top: 47px; }
  .card-front .lockup .web { font-size: 7px; letter-spacing: 0.2px; }
  .card-front .details { position: absolute; left: 129px; top: 32px; font-size: 7.8px; line-height: 10.5px; white-space: nowrap; }
  .card-front .details .email { font-size: 6.8px; }

  /* Business card — back */
  .card-back { position: absolute; left: 757px; top: 646px; width: 279px; height: 156px; border-radius: 9px 9px 9px 0; box-shadow: 2px 2px 0 var(--shadow); overflow: hidden; }
  .card-back .band { position: absolute; inset: 0; }
  .card-back .mark { position: absolute; left: 94px; top: 60px; display: flex; align-items: center; gap: 7px; }
  .card-back .mark .dot { width: 22px; height: 22px; border-radius: 50%; background: var(--paper); }
  .card-back .mark .name { font-size: 18px; line-height: 1; color: var(--paper); }
  .card-back .mark .sub { position: absolute; right: 0; top: 21px; font-size: 3px; color: var(--paper); white-space: nowrap; }
</style>
</head>
<body>

  <header class="brand-master">
    <span class="dot"></span>
    <span class="name">Quendrix</span>
    <span class="sub">TECHNOLOGIES INC.</span>
  </header>

  <section class="letterhead">
    <div class="band band-fill" role="img" aria-label="Decorative band of vertical green stripes"></div>
    <div class="lockup">
      <div class="row"><span class="dot"></span><span class="name">Quendrix</span></div>
      <div class="sub">TECHNOLOGIES INC.</div>
      <div class="web">www.quendrix.example</div>
    </div>
    <p class="address">47 Brindle Court, Suite 311<br>Toronto, ON M4K 2T8<br>P&nbsp; 647 512 7730<br>F&nbsp; 647 512 7731</p>
  </section>

  <section class="envelope">
    <div class="band band-fill" role="img" aria-label="Decorative band of vertical green stripes"></div>
    <div class="lockup">
      <div class="row"><span class="dot"></span><span class="name">Quendrix</span></div>
      <div class="sub">TECHNOLOGIES INC.</div>
      <div class="web">www.quendrix.example</div>
    </div>
    <p class="address">47 Brindle Court, Suite 311<br>Toronto, ON M4K 2T8<br>P&nbsp; 647 512 7730<br>F&nbsp; 647 512 7731</p>
  </section>

  <section class="card-front">
    <div class="lockup">
      <div class="row"><span class="dot"></span><span class="name">Quendrix</span></div>
      <div class="sub">TECHNOLOGIES INC.</div>
      <div class="web">www.quendrix.example</div>
    </div>
    <p class="details">Selvakumar (Selv) Nadarasan<br>Founder and CEO<br>47 Brindle Court, Suite 311<br>Toronto, ON M4K 2T8<br>P&nbsp; 647-512-7730<br>M 416-273-5094<br>F&nbsp; 647-512-7731<br><span class="email">selvakumar.nadarasan@mailbrook.example</span></p>
  </section>

  <section class="card-back">
    <div class="band band-fill" role="img" aria-label="Decorative field of vertical green stripes"></div>
    <div class="mark">
      <span class="dot"></span>
      <span class="name">Quendrix</span>
      <span class="sub">TECHNOLOGIES INC.</span>
    </div>
  </section>

</body>
</html>
```